Business Card Design

Please see my website www.lqvesting.com.au to for further information on my services and styling of my site

Project Deadline Extended
Reason: Deadline is extended to permit alterations to current designs or for any new submissions. Cheers

Industry/Entity Type

Business

Contact Information for Business Card

Marcus Theale
Empowerment Coach

'Live your passion'

marcus@lqvcoaching.com.au
0437518264
lqvcoaching.com.au

```html
<!DOCTYPE html>
<html lang="en">
<head>
<meta charset="utf-8">
<title>LQV Coaching – Business Card</title>
<link href="https://fonts.googleapis.com/css2?family=Open+Sans:wght@400;600;700&display=swap" rel="stylesheet">
<style>
  :root {
    --stage: #5a5e58;
    --card-white: #ffffff;
    --charcoal: #3d3d3f;
    --charcoal-light: #4a4a4c;
    --lime: #bfd730;
    --ink: #2b2b2b;
    --text-grey: #3a3a3a;
    --figure-grey: #d4d4d4;
    --figure-grey-soft: #ececec;
  }
  * { box-sizing: border-box; margin: 0; padding: 0; }
  html, body { width: 1200px; height: 1024px; overflow: hidden; }
  body {
    background: var(--stage);
    font-family: "Open Sans", Arial, sans-serif;
    position: relative;
  }
  .card {
    position: absolute;
    left: 234px;
    width: 748px;
    height: 425px;
    border-radius: 24px;
    overflow: hidden;
    background: var(--card-white);
  }
  .card--front { top: 79px; }
  .card--back { top: 547px; }

  .card__shapes { position: absolute; inset: 0; }

  .brand-name {
    position: absolute;
    left: 0;
    width: 588px;
    text-align: center;
    font-weight: 700;
    white-space: nowrap;
  }
  .card--front .brand-name {
    top: 58px;
    font-size: 44px;
    color: var(--lime);
  }
  .tagline {
    position: absolute;
    top: 186px; left: 0; width: 588px;
    text-align: center;
    font-size: 21px;
    color: var(--lime);
  }
  .person {
    position: absolute;
    top: 257px; left: 0; width: 588px;
    text-align: center;
    color: #fff;
  }
  .person__name { font-size: 25px; font-weight: 700; letter-spacing: 0.5px; text-transform: uppercase; }
  .person__role { font-size: 17px; margin-top: 2px; }

  .contact {
    position: absolute;
    display: flex;
    align-items: center;
    gap: 12px;
    color: var(--ink);
    font-size: 17px;
  }
  .contact--phone { left: 74px; top: 372px; }
  .contact--web { left: 404px; top: 363px; line-height: 21px; }
  .contact svg { flex: none; }

  .card--back .brand-name {
    left: 300px; width: 400px;
    top: 150px;
    font-size: 50px;
    color: var(--text-grey);
  }
  .service {
    position: absolute;
    top: 384px;
    font-size: 19px;
    color: var(--text-grey);
  }
  .service--strength { left: 175px; }
  .service--coaching { right: 30px; }
</style>
</head>
<body>

<section class="card card--front">
  <svg class="card__shapes" width="748" height="425" viewBox="0 0 748 425">
    <defs>
      <linearGradient id="panel-shade" x1="0" y1="0" x2="0" y2="1">
        <stop offset="0" stop-color="#454547"/>
        <stop offset="1" stop-color="#363638"/>
      </linearGradient>
      <linearGradient id="figure-fade-front" x1="0" y1="0" x2="0" y2="1">
        <stop offset="0" stop-color="var(--figure-grey-soft)"/>
        <stop offset="1" stop-color="var(--figure-grey)"/>
      </linearGradient>
    </defs>
    <rect class="figure-area" x="600" y="30" width="148" height="323" fill="url(#figure-fade-front)" role="img" aria-label="Light grey silhouette of a person with arms raised"/>
    <path class="dark-panel" d="M0 0 H540 C600 70 625 170 612 221 C602 280 596 320 588 353 H0 Z" fill="url(#panel-shade)"/>
    <rect class="contact-band" x="0" y="353" width="748" height="72" fill="var(--lime)"/>
  </svg>

  <div class="brand-name">LQV Coaching</div>
  <div class="tagline">“Live Your Passion”</div>
  <div class="person">
    <div class="person__name">Marcus Theale</div>
    <div class="person__role">Empowerment Coach</div>
  </div>

  <div class="contact contact--phone">
    <svg width="18" height="18" viewBox="0 0 24 24" aria-hidden="true"><path fill="var(--ink)" d="M6.6 10.8a15.1 15.1 0 0 0 6.6 6.6l2.2-2.2a1 1 0 0 1 1-.25 11.4 11.4 0 0 0 3.6.6 1 1 0 0 1 1 1V20a1 1 0 0 1-1 1A17 17 0 0 1 3 4a1 1 0 0 1 1-1h3.5a1 1 0 0 1 1 1c0 1.25.2 2.45.6 3.6a1 1 0 0 1-.25 1z"/></svg>
    <span>0437518264</span>
  </div>
  <div class="contact contact--web">
    <svg width="24" height="24" viewBox="0 0 24 24" aria-hidden="true"><g fill="none" stroke="var(--ink)" stroke-width="1.8"><circle cx="12" cy="12" r="10"/><ellipse cx="12" cy="12" rx="4.5" ry="10"/><path d="M2 12h20M4 6.5h16M4 17.5h16"/></g></svg>
    <span>marcus@lqvcoaching.com.au<br>lqvcoaching.com.au</span>
  </div>
</section>

<section class="card card--back">
  <svg class="card__shapes" width="748" height="425" viewBox="0 0 748 425">
    <defs>
      <linearGradient id="figure-fade-back" x1="0" y1="0" x2="0" y2="1">
        <stop offset="0" stop-color="var(--figure-grey-soft)"/>
        <stop offset="1" stop-color="var(--figure-grey)"/>
      </linearGradient>
    </defs>
    <rect class="figure-area" x="0" y="25" width="200" height="400" fill="url(#figure-fade-back)" role="img" aria-label="Large light grey silhouette of a person with both arms raised"/>
  </svg>

  <div class="brand-name">LQV Coaching</div>
  <div class="service service--strength">Strength &amp; Conditioning</div>
  <div class="service service--coaching">Empowerment Coaching</div>
</section>

</body>
</html>
```